Brightway Gym Castlemore (Annual sale ONLY $8.95 per week!)

We are after a new fresh design for our annual promo! we need a design that can be used for core flute signs (1200 x 2400), Facebook posts, Instagram posts, posters and any advertising we do throughout our 12 week campaign!

In the past we have gone for a suit all vibe when it comes to advertising with images of people training and looking happy and excited. As we pride ourselves in being a gym for everyone.

Information and text that need to be included in the designs.
Please include logo on each design (attached) also happy with logo color's to be changed to suit designs.

We normally do 2 x core flute designs, one that has the picture and information regarding the sale and another big bold one that shows 50% off to really grab the eye of passing traffic.
Core flute #1
- $8.95 per week*
- Only 100 memberships available!
- Terms and conditions apply*

Core flute #2
- 50% OFF sale
- Annual sale
- Pay nothing for 30 days!

Poster (use in club and local businesses
- $8.95 per week*
- No Joining fees
- 24/7 access

Facebook and Instagram posts
- 50% OFF
- $8.95 per week*
- No joining fees

```html
<!DOCTYPE html>
<html lang="en">
<head>
<meta charset="utf-8">
<title>Brightway Gym Castlemore – $8.95 per week</title>
<link href="https://fonts.googleapis.com/css2?family=Montserrat:wght@700;800;900&display=swap" rel="stylesheet">
<style>
  :root {
    --ink: #0b0b0c;
    --red: #e3141b;
    --red-deep: #b50e13;
    --white: #ffffff;
    --grey: #8a8a8e;
    --photo-warm: #6b5346;
    --photo-dark: #2a2322;
  }
  * { margin: 0; padding: 0; box-sizing: border-box; }
  html, body { width: 1200px; height: 2404px; overflow: hidden; background: var(--ink); }
  body { font-family: "Montserrat", Arial, sans-serif; color: var(--white); }

  .sign { position: relative; width: 1200px; height: 2404px; overflow: hidden; background: var(--ink); }

  .training-photo {
    position: absolute; left: 0; top: 0; width: 1200px; height: 1560px;
    background:
      radial-gradient(ellipse 520px 700px at 380px 760px, rgba(190,140,115,0.55), transparent 70%),
      radial-gradient(ellipse 420px 600px at 860px 640px, rgba(200,150,130,0.45), transparent 70%),
      linear-gradient(180deg, var(--photo-dark) 0%, var(--photo-warm) 40%, #3a2e2a 70%, var(--ink) 100%);
  }

  .decor { position: absolute; inset: 0; width: 1200px; height: 2404px; }

  .brand {
    position: absolute; left: 150px; top: 118px;
    display: flex; align-items: center; gap: 26px;
  }
  .brand-dot { width: 136px; height: 136px; border-radius: 50%; background: var(--red); flex: none; }
  .brand-name { font-weight: 800; font-size: 78px; letter-spacing: -1px; color: var(--white); line-height: 1; white-space: nowrap; }

  .price-tag {
    position: absolute; left: 230px; top: 1390px; width: 700px; height: 230px;
    background: var(--red); transform: rotate(-7deg);
    display: flex; align-items: center; justify-content: center;
  }
  .price-tag span { font-weight: 900; font-size: 200px; letter-spacing: -4px; line-height: 1; }

  .period-tag {
    position: absolute; left: 200px; top: 1600px; width: 760px; height: 200px;
    background: var(--white); transform: rotate(-7deg);
    display: flex; align-items: center; justify-content: center;
  }
  .period-tag span { font-weight: 900; font-size: 110px; color: var(--red); line-height: 1; letter-spacing: -1px; white-space: nowrap; }

  .offer-note {
    position: absolute; left: 0; width: 1200px; top: 1950px;
    text-align: center; font-weight: 800; font-size: 62px; line-height: 1.25;
  }
  .terms {
    position: absolute; left: 0; width: 1200px; top: 2245px;
    text-align: center; font-weight: 700; font-size: 32px;
  }
</style>
</head>
<body>
<main class="sign">
  <div class="training-photo" role="img" aria-label="Photo of a man and a woman running side by side in a dimly lit gym"></div>

  <svg class="decor" viewBox="0 0 1200 2404" aria-hidden="true">
    <polygon points="1010,0 1050,0 1050,260 1010,300" fill="var(--red)"/>
    <polygon points="1070,0 1090,0 1090,220 1070,240" fill="var(--white)" opacity="0.85"/>
    <polygon points="1110,0 1150,0 1150,340 1110,380" fill="var(--red)"/>
    <polygon points="1170,0 1200,0 1200,180 1170,210" fill="var(--grey)" opacity="0.6"/>
    <rect x="0" y="380" width="60" height="820" fill="var(--grey)" opacity="0.25"/>
    <polygon points="1000,1500 1040,1450 1040,2404 1000,2404" fill="var(--red)"/>
    <polygon points="1060,1380 1080,1355 1080,2404 1060,2404" fill="var(--white)" opacity="0.8"/>
    <polygon points="1100,1320 1150,1260 1150,2404 1100,2404" fill="var(--red)"/>
    <polygon points="1165,1420 1200,1380 1200,2404 1165,2404" fill="var(--red-deep)"/>
    <polygon points="960,2170 980,2145 980,2404 960,2404" fill="var(--grey)" opacity="0.5"/>
  </svg>

  <header class="brand">
    <div class="brand-dot"></div>
    <div class="brand-name">Brightway Gym</div>
  </header>

  <div class="price-tag"><span>$8.95</span></div>
  <div class="period-tag"><span>PER WEEK*</span></div>

  <p class="offer-note">Only 100 memberships<br>available!</p>
  <p class="terms">Terms and conditions apply*</p>
</main>
</body>
</html>
```